Financial Service Company Need Business Card Design

This is a new startup company, first of its kind to offer this service. We facilitate the movement of deposit funds electronically between home buyers and real estate brokerages.Our customers are REALTORS®, real estate brokerages, and home buyers, we identify ourselves as a financial/technology company.
Not looking for anything too flashy. Just a clean design that shows the logo, contact info, etc. Company colors can be seen on attached logo, and 'coming soon page'
www.plumvault.ca
Industry/Entity Type
Business
Contact Information for Business Card

```html
<!DOCTYPE html>
<html lang="en">
<head>
<meta charset="utf-8">
<title>PlumVault Business Card</title>
<link href="https://fonts.googleapis.com/css2?family=Open+Sans:wght@400;600;700&display=swap" rel="stylesheet">
<style>
  :root {
    --backdrop: #9a9e9d;
    --card-white: #ffffff;
    --brand-gray: #6b696b;
    --text-gray: #5f5e60;
    --brand-orange: #e8502a;
    --light-text: #ffffff;
  }
  * { box-sizing: border-box; margin: 0; padding: 0; }
  html, body { width: 1200px; height: 900px; overflow: hidden; }
  body {
    background: var(--backdrop);
    font-family: "Open Sans", sans-serif;
    position: relative;
  }
  .card {
    position: absolute;
    width: 510px;
    height: 292px;
    top: 304px;
    overflow: hidden;
  }
  .card-front { left: 70px; background: var(--card-white); }
  .card-back { left: 620px; background: var(--brand-gray); }

  .wordmark {
    display: flex;
    align-items: center;
    justify-content: center;
    gap: 12px;
    font-weight: 600;
  }
  .wordmark-square {
    width: 26px; height: 26px;
    background: var(--brand-orange);
  }
  .card-front .wordmark {
    position: absolute; top: 40px; left: 0; right: 0;
    color: var(--text-gray);
    font-size: 38px;
  }
  .card-back .wordmark {
    height: 100%;
    color: var(--light-text);
    font-size: 44px;
  }
  .card-back .wordmark-square { width: 30px; height: 30px; }

  .holder {
    position: absolute; left: 172px; top: 118px;
  }
  .holder-name {
    color: var(--brand-orange);
    font-weight: 700;
    font-size: 19px;
    line-height: 1.1;
  }
  .holder-function {
    color: var(--text-gray);
    font-size: 13px;
    line-height: 1.2;
  }
  .holder-mobile {
    margin-top: 8px;
    color: var(--text-gray);
    font-size: 14px;
  }
  .label { color: var(--brand-orange); font-weight: 700; margin-right: 4px; }

  .accent-band {
    position: absolute; left: 0; right: 0; top: 204px; height: 12px;
    background: var(--brand-orange);
  }
  .contact-strip {
    position: absolute; left: 0; right: 0; top: 216px; bottom: 0;
    background: var(--brand-gray);
    color: var(--light-text);
    font-size: 12.5px;
    line-height: 1.45;
  }
  .address { position: absolute; left: 62px; top: 14px; }
  .online { position: absolute; right: 42px; top: 30px; }
</style>
</head>
<body>
  <section class="card card-front" aria-label="Business card front">
    <div class="wordmark"><span class="wordmark-square"></span><span>PlumVault</span></div>
    <div class="holder">
      <p class="holder-name">Name Surname</p>
      <p class="holder-function">Function</p>
      <p class="holder-mobile"><span class="label">M.</span>1234567890</p>
    </div>
    <div class="accent-band"></div>
    <div class="contact-strip">
      <p class="address"><span class="label">A.</span>123 Main st.<br>Anytown CA 12345-6789<br>USA</p>
      <p class="online"><span class="label">W.</span>www.plumvault.ca<br><span class="label">E.</span>info@plumvault.ca</p>
    </div>
  </section>

  <section class="card card-back" aria-label="Business card back">
    <div class="wordmark"><span class="wordmark-square"></span><span>PlumVault</span></div>
  </section>
</body>
</html>
```